Belmir, Dunholt & Belmir Concussion Infographic

We need an infographic for a Belmir, Dunholt & Belmir, a personal injury law firm based in Florida. Our goal is to raise awareness about concussions targeted towards young teens. We have researched and gathered info on the symptoms, danger signs, what to do and not do after sustaining a concussion, and additional facts on the severity of concussions. Our main goal for this infographic is to create a well-designed, easy-to-read infographic that is visually appealing. The more graphics we can use to aid with the statistics we are offering, the better. What we don't want is just an infographic with a bunch of facts listed without any visual aids. We need a creative way to capture the audiences attention through eye-catching visuals so they will be enticed to read the statistics in the infographic.

Target Market(s)

high school sports teams, youth sports leagues,

Industry/Entity Type

Legal

Font styles to use
Serif

Colors
0355a3
33a6d7
ffffff
fece3e

Requirements
Must have
• Visual aids that compliment our stats, visually appealing imagery, cite our sources at the bottom of the infographic in fine print
Nice to have
• creative and visual ways to back up statistics, contains a flow both cognitively and visually - like a good story, conveying a message at a glance - taking alot of data and boiling it down to one image,
Should not have
• any pictures or visuals that may scare or turn off audience,

```html
<!DOCTYPE html>
<html lang="en">
<head>
<meta charset="utf-8">
<title>Belmir, Dunholt &amp; Belmir – What Is a Concussion?</title>
<link rel="stylesheet" href="https://fonts.googleapis.com/css2?family=Montserrat:wght@700;800;900&family=Noto+Serif:wght@400;700&family=Roboto:wght@400;700;900&display=swap">
<style>
:root{
  --navy:#0355a3;
  --sky:#33a6d7;
  --white:#ffffff;
  --gold:#fece3e;
  --ink:#0b1220;
  --danger:#e5242b;
  --do-1:#d6e02c;
  --do-2:#8cc63f;
  --do-3:#45b048;
  --do-4:#0a9a4a;
  --avoid-1:#f6a43f;
  --avoid-2:#f58733;
  --avoid-3:#ef5a2b;
  --deep:#0a1e3a;
}
*{margin:0;padding:0;box-sizing:border-box}
html,body{width:1200px;height:3607px;overflow:hidden;background:var(--ink)}
.canvas{position:relative;width:1200px;height:3607px;overflow:hidden;
  background:radial-gradient(ellipse at 50% 35%,#12325c 0%,#081528 55%,#050b16 100%);
  font-family:"Roboto",Arial,sans-serif;color:var(--white)}
.abs{position:absolute}

/* header */
.header{left:0;top:0;width:1200px;height:615px;background:linear-gradient(#050505,#0b0f18)}
.brand{left:48px;top:58px;font-family:"Noto Serif",Georgia,serif;font-weight:700;font-size:32px;line-height:1.05;color:var(--white);letter-spacing:1px}
.brain-art{left:440px;top:0;width:320px;height:290px;border-radius:0 0 160px 160px;
  background:radial-gradient(circle at 50% 40%,#c9773a 0%,#7a3a18 45%,#1a0c06 80%,transparent 100%)}
.kicker{left:0;width:1200px;top:332px;text-align:center;padding-right:280px;font-family:"Montserrat",sans-serif;font-weight:900;font-size:62px;color:var(--white)}
.title{left:0;width:1200px;top:400px;text-align:center;font-family:"Montserrat",sans-serif;font-weight:900;font-size:138px;line-height:1;color:var(--gold);letter-spacing:2px}
.definition{left:60px;width:1080px;top:532px;text-align:center;font-family:"Noto Serif",Georgia,serif;font-size:27px;line-height:1.35;color:var(--white)}
.definition em{font-style:normal;color:var(--gold)}

/* symptoms */
.symptoms{left:0;top:615px;width:1200px;height:445px;background:var(--navy)}
.band-title{width:1200px;left:0;text-align:center;font-family:"Montserrat",sans-serif;font-weight:800;font-size:82px;line-height:1}
.symptoms .band-title{top:40px;color:var(--gold)}
.icon-item{width:228px;text-align:center}
.icon-item .disc{display:block;margin:0 auto;width:156px;height:156px;border-radius:50%}
.symptoms .disc{background:var(--gold)}
.icon-item p{margin-top:12px;font-weight:700;font-size:25px;line-height:1.1}
.symptoms p{color:var(--gold)}

/* danger */
.danger{left:0;top:1060px;width:1200px;height:430px;background:var(--danger)}
.danger .band-title{top:38px;color:var(--white)}
.danger .disc{background:var(--white);width:168px;height:168px}
.danger p{color:#ffe7a6;font-size:26px}

/* what to do */
.tech-bg{left:0;top:1490px;width:1200px;height:1950px;
  background:radial-gradient(ellipse at 20% 40%,rgba(51,166,215,.25),transparent 55%),radial-gradient(ellipse at 85% 70%,rgba(51,166,215,.2),transparent 55%)}
.section-tag{height:110px;background:var(--white);border-radius:26px;display:flex;align-items:center;justify-content:center;gap:18px;white-space:nowrap;
  font-family:"Montserrat",sans-serif;font-weight:900;font-size:46px}
.tag-do{left:380px;width:440px;top:1540px;color:var(--do-3)}
.tag-avoid{top:2310px;left:360px;width:500px;color:var(--danger)}
.rail{border:8px solid var(--white)}
.rail-do{left:108px;top:1594px;width:280px;border-right:none;border-bottom:none;border-radius:30px 0 0 0}
.step{height:108px;border-radius:0 54px 54px 0;display:flex;align-items:center;color:var(--deep);font-weight:900}
.step .num{flex:none;width:96px;height:96px;margin-left:-40px;border-radius:50%;background:var(--white);display:flex;align-items:center;justify-content:center;font-family:"Montserrat",sans-serif;font-size:50px;color:var(--navy)}
.step .text{flex:1;min-width:0;padding-left:28px;font-size:28px;line-height:1.12}
.step .text b{text-transform:uppercase}
.step .text span{font-weight:700}
.step .art{flex:none;width:140px;height:86px;margin-right:20px;border-radius:10px;background:rgba(255,255,255,.9)}
.step-1{background:var(--do-1)}
.step-2{background:var(--do-2)}
.step-3{background:var(--do-3);color:var(--white)}
.step-4{background:var(--do-4);color:var(--white)}

/* avoid */
.rail-avoid{left:860px;top:2366px;width:240px;height:700px;border-left:none;border-bottom:none;border-radius:0 30px 0 0}
.rail-avoid-end{left:1040px;top:3058px;width:60px;height:8px;background:var(--white)}
.avoid{height:108px;border-radius:54px 0 0 54px;display:flex;align-items:center;color:var(--deep)}
.avoid .art{flex:none;width:120px;height:108px;border-radius:54px 0 0 54px;background:rgba(255,255,255,.25)}
.avoid .text{flex:1;min-width:0;text-align:right;padding-right:30px;font-weight:900;font-size:29px;line-height:1.15}
.avoid .text span{display:block}
.avoid .num{flex:none;width:96px;height:96px;margin-right:-40px;border-radius:50%;background:var(--white);display:flex;align-items:center;justify-content:center;font-family:"Montserrat",sans-serif;font-weight:900;font-size:50px;color:var(--avoid-3)}
.avoid-1{background:var(--avoid-1)}
.avoid-2{background:var(--avoid-2)}
.avoid-3{background:var(--avoid-3)}

/* stats */
.stat{width:216px;text-align:center}
.stat .ring{position:relative;width:205px;height:205px;margin:0 auto;border-radius:50%;background:var(--white);display:flex;flex-direction:column;align-items:center;justify-content:flex-end;padding-bottom:26px;color:var(--navy);font-family:"Montserrat",sans-serif;font-weight:900}
.stat .big{font-size:30px;line-height:1;background:var(--sky);color:var(--white);padding:8px 10px 4px;border-radius:8px}
.stat .small{font-size:17px;background:var(--sky);color:var(--gold);padding:0 10px 6px;border-radius:0 0 8px 8px}
.stat .label{margin:-10px auto 0;width:200px;height:112px;background:var(--gold);border-radius:0 0 20px 20px;border:5px solid var(--sky);border-top:none;display:flex;align-items:center;justify-content:center;text-align:center;padding:10px 8px 0;color:var(--navy);font-weight:900;font-size:20px;line-height:1.1}
.stat .label em{font-style:normal;color:var(--sky)}
.ring-fill{background:var(--sky)!important;color:var(--white)!important;justify-content:center!important;padding:0!important;font-size:34px;line-height:1}
.ring-gold{background:var(--navy)!important;border:12px solid var(--gold);color:var(--gold)!important;justify-content:center!important;padding:0!important;font-size:38px}
.ring-clock{justify-content:center!important;padding:0!important}

/* warning */
.warning{left:80px;top:3352px;width:1060px;display:flex;align-items:center;gap:30px}
.warning p{font-weight:900;font-size:30px;line-height:1.3;color:var(--gold)}

/* sources */
.sources{left:0;top:3472px;width:1200px;height:135px;background:#0b2550;text-align:center;font-weight:700;font-size:19px;line-height:1.35;padding-top:12px;color:var(--white)}
</style>
</head>
<body>
<div class="canvas">

  <header class="abs header"></header>
  <div class="abs brand">BELMIR, DUNHOLT<br>&amp; BELMIR</div>
  <div class="abs brain-art" role="img" aria-label="Glowing illustration of a human head with the brain visible"></div>
  <div class="abs kicker">WHAT IS A</div>
  <h1 class="abs title">CONCUSSION?</h1>
  <p class="abs definition">A <em>TRAUMATIC</em> brain injury, resulting from a <em>BLOW TO THE HEAD</em> or <em>BODY</em>, that causes the brain to jerk back and forth within the skull.</p>

  <section class="abs symptoms">
    <h2 class="abs band-title">symptoms</h2>
    <div class="abs icon-item" style="left:30px;top:155px"><span class="disc" role="img" aria-label="Icon of a dizzy person"></span><p>dizziness or lack of balance</p></div>
    <div class="abs icon-item" style="left:258px;top:155px"><span class="disc" role="img" aria-label="Icon of a person holding their head"></span><p>Headache or "Pressure" in head</p></div>
    <div class="abs icon-item" style="left:486px;top:155px"><span class="disc" role="img" aria-label="Icon of a nauseous person"></span><p>nauseau or vomiting</p></div>
    <div class="abs icon-item" style="left:714px;top:155px"><span class="disc" role="img" aria-label="Icon of a slumped, tired person"></span><p>Feeling hazy, sluggish, foggy or groggy</p></div>
    <div class="abs icon-item" style="left:942px;top:155px"><span class="disc" role="img" aria-label="Icon of a confused person"></span><p>confusion, lack of concentration, memory problems</p></div>
  </section>

  <section class="abs danger">
    <h2 class="abs band-title">danger signs</h2>
    <div class="abs icon-item" style="left:54px;top:150px"><span class="disc" role="img" aria-label="Icon of a person with a painful headache"></span><p>Persistent Headache</p></div>
    <div class="abs icon-item" style="left:283px;top:150px"><span class="disc" role="img" aria-label="Icon of a drowsy person"></span><p>drowsiness</p></div>
    <div class="abs icon-item" style="left:530px;top:150px;width:260px"><span class="disc" role="img" aria-label="Icon of two eyes with unequal pupils"></span><p>one pupil larger than the other</p></div>
    <div class="abs icon-item" style="left:830px;top:150px;width:320px"><span class="disc" role="img" aria-label="Icon of a person losing consciousness"></span><p>Loss of consciousness more than a minute</p></div>
  </section>

  <div class="abs tech-bg" role="img" aria-label="Soft glowing blue technology background"></div>

  <div class="abs rail rail-do" style="height:560px"></div>
  <div class="abs section-tag tag-do">
    <svg width="52" height="62" viewBox="0 0 52 62" aria-hidden="true"><rect x="4" y="8" width="44" height="50" rx="5" fill="none" stroke="currentColor" stroke-width="5"/><rect x="16" y="3" width="20" height="10" rx="3" fill="currentColor"/><path d="M14 34 l9 9 l16 -18" fill="none" stroke="currentColor" stroke-width="6" stroke-linecap="round" stroke-linejoin="round"/></svg>
    <span>WHAT TO DO</span>
  </div>

  <div class="abs step step-1" style="left:148px;top:1660px;width:956px"><span class="num">1.</span><span class="text"><b>Remove athlete from play.</b><br><span>Look out for signs of a concussion.</span></span><span class="art" role="img" aria-label="Illustration of an injured athlete being helped"></span></div>
  <div class="abs step step-2" style="left:148px;top:1792px;width:956px"><span class="num">2.</span><span class="text"><b>Seek medical attention</b><br><span>from a health care professional.</span></span><span class="art" style="background:rgba(0,0,0,.15)" role="img" aria-label="Illustration of a doctor and patient"></span></div>
  <div class="abs step step-3" style="left:148px;top:1922px;width:956px;height:116px"><span class="num">3.</span><span class="text"><b>Rest well</b> <span>and let the brain heal.<br>Physically or mentally demanding activities may worsen symptoms.</span></span><span class="art" style="background:rgba(0,0,0,.35)" role="img" aria-label="Illustration of a person resting"></span></div>
  <div class="abs step step-4" style="left:148px;top:2052px;width:956px"><span class="num">4.</span><span class="text"><b>Educate</b> <span>Parents and students and share more information about concussions.</span></span><span class="art" style="background:rgba(0,0,0,.35)" role="img" aria-label="Illustration of a classroom presentation"></span></div>

  <div class="abs rail rail-avoid"></div>
  <div class="abs section-tag tag-avoid">
    <svg width="56" height="56" viewBox="0 0 56 56" aria-hidden="true"><circle cx="28" cy="28" r="24" fill="none" stroke="currentColor" stroke-width="6"/><path d="M19 19 l18 18 M37 19 l-18 18" stroke="currentColor" stroke-width="7" stroke-linecap="round"/></svg>
    <span>WHAT TO AVOID</span>
  </div>

  <div class="abs avoid avoid-1" style="left:96px;top:2470px;width:960px"><span class="art" role="img" aria-label="Icon of a person on an exercise bike"></span><span class="text"><b>DEMANDING PHYSICAL ACTIVITIES.</b><span>They may worsen symptoms.</span></span><span class="num">1.</span></div>
  <div class="abs avoid avoid-2" style="left:96px;top:2600px;width:960px"><span class="art" role="img" aria-label="Icon of a head with mental activity"></span><span class="text"><b>STRENUOUS MENTAL ACTIVITY e.g.</b><span>computer work, reading etc.</span></span><span class="num">2.</span></div>
  <div class="abs avoid avoid-3" style="left:96px;top:2730px;width:960px"><span class="art" role="img" aria-label="Icon of a crossed-out car and driver"></span><span class="text"><b>DO NOT DRIVE for at least 24hours</b><span>to minimize risk of accident.</span></span><span class="num">3.</span></div>

  <div class="abs stat" style="left:36px;top:2975px"><div class="ring" role="img" aria-label="Silhouettes of running athletes above the figure"><span class="big">1.6 - 3.8<br><small style="font-size:18px">MILLION</small></span><span class="small">PER YEAR</span></div><div class="label"><span>Sports-Related Concussions</span></div></div>
  <div class="abs stat" style="left:264px;top:2975px"><div class="ring" role="img" aria-label="Silhouettes of high school football players above the figure"><span class="big">300,000</span><span class="small">PER YEAR</span></div><div class="label"><span>Concussions in High School Athletes</span></div></div>
  <div class="abs stat" style="left:492px;top:2975px"><div class="ring ring-fill">90% or<br>MORE</div><div class="label"><span>Concussions occuring WITHOUT losing consciousness</span></div></div>
  <div class="abs stat" style="left:720px;top:2975px"><div class="ring ring-gold">80-90%</div><div class="label"><span>Typically resolve in 7 - 10 DAYS</span></div></div>
  <div class="abs stat" style="left:948px;top:2975px"><div class="ring ring-clock"><svg width="160" height="160" viewBox="0 0 160 160" aria-hidden="true"><circle cx="80" cy="80" r="72" fill="var(--navy)"/><circle cx="80" cy="80" r="60" fill="#fff"/><path d="M80 80 V24 A56 56 0 0 1 136 80 Z" fill="var(--gold)"/><path d="M80 80 V34 M80 80 H124" stroke="var(--navy)" stroke-width="10" stroke-linecap="round"/></svg></div><div class="label"><span>Recovery time is longer in <em>teens</em> than in <em>adults</em></span></div></div>

  <div class="abs warning">
    <svg width="110" height="96" viewBox="0 0 110 96" aria-hidden="true"><path d="M55 4 L106 92 H4 Z" fill="var(--gold)" stroke="var(--danger)" stroke-width="8" stroke-linejoin="round"/><rect x="49" y="30" width="12" height="36" rx="5" fill="var(--danger)"/><circle cx="55" cy="78" r="6" fill="var(--danger)"/></svg>
    <p>An athlete who has had a concussion in the past is<br>3-6 TIMES MORE LIKELY to suffer another concussion.</p>
  </div>

  <footer class="abs sources">
    Northgate Health<br>
    http://brainwise-facts.org/concussions-101/statistics/<br>
    National Council for Youth Injury Prevention and Safety Research (NCYIPSR)<br>
    https://health.riverbendclinic.org/2012/08/suspect-a-concussion-what-you-need-to-know/
  </footer>
</div>
</body>
</html>
```